Online plant nursery needs3 seperate slides for a intro web site slide slide show

We need 3 slide graphics / banners measurments should be 960wide 540 tall and 2mb or smaller. We are an online mail order nursery that focuses sales on Peonies.
Slide 1: Use faded out photos of Peony Garden with many flowers just budding. Our logo and the Words "A Lost Spring is Never Found Again". try to use our logo in a small small watermark on all slides.
Slide 2: Use your own creativity for the slide.... message should say "Free Shipping"
Slide 3: Use your own creativity for the slide .... messgae "Shop Our Other Items". To see site it will be used on go to http://k4830157.tbrwxq9pnlhe.preview82.shopnestle-example.com/

Target Market(s)

home owners age 30 - 65.

Industry/Entity Type

Nursery

Requirements
Must have
• must transition well.
Should not have
• can not be larger than 2MB per file

```html
<!DOCTYPE html>
<html lang="en">
<head>
<meta charset="utf-8">
<title>Hollowbrook Nursery – Free Shipping</title>
<link href="https://fonts.googleapis.com/css2?family=Dancing+Script:wght@400&family=Marcellus&family=Archivo+Narrow:wght@400;700&display=swap" rel="stylesheet">
<style>
  :root {
    --page: #ffffff;
    --ink: #1e1e1e;
    --muted: #555555;
    --rule: #d9d9d9;
    --accent: #e0407f;
    --sale: #e8424a;
    --placeholder: #e6e6e6;
    --leaf: #5e9a2e;
    --leaf-light: #a9cf6a;
    --bloom: #e9559a;
    --bloom-soft: #f6c9dd;
  }
  * { box-sizing: border-box; margin: 0; padding: 0; }
  html, body { width: 1200px; height: 1200px; overflow: hidden; background: var(--page); }
  body { position: relative; font-family: "Archivo Narrow", "Arial Narrow", sans-serif; color: var(--ink); }

  .site-header { position: absolute; left: 120px; top: 0; width: 960px; height: 125px; border-bottom: 1px solid var(--rule); }
  .search-icon { position: absolute; left: 20px; top: 52px; width: 22px; height: 22px; }
  .brand { position: absolute; left: 50%; top: 46px; transform: translateX(-50%); white-space: nowrap; }
  .brand-name { font-family: "Marcellus", serif; font-size: 28px; color: var(--ink); letter-spacing: .04em; }
  .account-links { position: absolute; right: 10px; top: 84px; display: flex; gap: 20px; font-size: 12px; font-weight: 700; letter-spacing: .02em; align-items: center; }
  .account-links .star { color: var(--sale); }
  .account-links .cart { color: var(--sale); display: flex; align-items: center; gap: 4px; }

  .main-nav { position: absolute; left: 120px; top: 126px; width: 960px; height: 56px; border-bottom: 1px solid var(--rule); display: flex; justify-content: center; align-items: center; gap: 40px; font-size: 15px; font-weight: 700; letter-spacing: .03em; }
  .main-nav .active { text-decoration: underline; }

  .hero-slide { position: absolute; left: 120px; top: 200px; width: 960px; height: 540px; overflow: hidden; }
  .hero-photo { position: absolute; inset: 0;
    background: linear-gradient(100deg, var(--leaf) 0%, var(--leaf-light) 30%, #f4f1ee 52%, var(--bloom-soft) 72%, var(--bloom) 88%, #ffffff 100%); }
  .hero-frame { position: absolute; inset: 0; }
  .hero-message { position: absolute; left: 220px; top: 246px; width: 554px; text-align: center; font-family: "Dancing Script", cursive; font-size: 40px; color: var(--accent); }
  .hero-watermark { position: absolute; left: 0; right: 0; bottom: 20px; text-align: center; font-family: "Marcellus", serif; font-size: 16px; letter-spacing: .04em; color: #ffffff; }

  .product { position: absolute; font-size: 13px; line-height: 1.45; }
  .product-title { font-weight: 700; letter-spacing: .02em; }
  .product-sale { color: var(--sale); }
  .product-thumb { position: absolute; background: var(--placeholder); width: 160px; height: 60px; }
  .more-info { position: absolute; font-size: 12px; color: var(--muted); }
  .more-info::before { content: "▸"; margin-right: 3px; }
</style>
</head>
<body>
  <header class="site-header">
    <svg class="search-icon" viewBox="0 0 22 22" aria-label="Search">
      <circle cx="13" cy="9" r="6" fill="none" stroke="#e8424a" stroke-width="2.2"/>
      <line x1="8.5" y1="13.5" x2="2" y2="20" stroke="#e8424a" stroke-width="2.6" stroke-linecap="round"/>
    </svg>
    <div class="brand">
      <span class="brand-name">Hollowbrook Nursery</span>
    </div>
    <nav class="account-links">
      <span>MY ACCOUNT</span>
      <span><span class="star">★</span> WISH LIST</span>
      <span class="cart">
        <svg width="13" height="13" viewBox="0 0 13 13"><path d="M3 4V3a3.5 3 0 0 1 7 0v1" fill="none" stroke="#e8424a" stroke-width="1.4"/><rect x="1" y="4" width="11" height="8.5" fill="#e8424a"/></svg>
        (0)
      </span>
    </nav>
  </header>

  <nav class="main-nav">
    <span>BICOLOR</span>
    <span class="active">INTERSECTIONAL PEONIES</span>
    <span>TREE PEONY</span>
    <span>RED</span>
    <span>PINK</span>
    <span>WHITE</span>
    <span>YELLOW</span>
  </nav>

  <section class="hero-slide">
    <div class="hero-photo" role="img" aria-label="Photo of a wicker basket filled with fresh pink peonies carried across a green garden lawn"></div>
    <svg class="hero-frame" viewBox="0 0 960 540">
      <path d="M242 115 H752 A22 22 0 0 0 774 137 V405 A22 22 0 0 0 752 427 H242 A22 22 0 0 0 220 405 V137 A22 22 0 0 0 242 115 Z" fill="#ffffff" fill-opacity="0.62" stroke="#ffffff" stroke-width="3"/>
      <path d="M250 124 H744 A20 20 0 0 0 765 145 V397 A20 20 0 0 0 744 418 H250 A20 20 0 0 0 229 397 V145 A20 20 0 0 0 250 124 Z" fill="none" stroke="#3a3a3a" stroke-width="1.2"/>
    </svg>
    <div class="hero-message">Free Shipping</div>
    <div class="hero-watermark">Hollowbrook Nursery</div>
  </section>

  <div class="product" style="left:120px; top:760px;">
    <div class="product-title">SAMPLE PRODUCT THREE</div>
    <div>Our Price: $95.00</div>
    <div class="product-sale">Sale Price: $76.00</div>
  </div>
  <div class="product-thumb" style="left:270px; top:830px;"></div>

  <div class="more-info" style="left:520px; top:826px;">more info</div>
  <div class="product" style="left:590px; top:806px;">
    <div class="product-title">SAMPLE PRODUCT TWO</div>
    <div>Our Price: $75.00</div>
    <div class="product-sale">Sale Price: $55.00</div>
  </div>
  <div class="product-thumb" style="left:760px; top:880px;"></div>

  <div class="more-info" style="left:1010px; top:880px;">more info</div>
</body>
</html>
```